Kestrelvale High School Association Website New Design

We require a fresh new website design for the Kestrelvale High School Old Boys Association. The association is a non-for-profit and as such we like the site to reflect the ethos.
We require a design that uses responsive design techniques, so to allow the site to shift between mobile, tablet and desktop spaces and maintain elements in the site.
We would like a landing/home page design, and also an inner news/article based design included.
We want the site to appeal to a broad market of both the old guard members but also to bring on board the new social savey younger members.
The site needs to have a modern take on a professional yet fresh and opulent/elegant look.
A site that we like influences from is http://www.varonelle-kestra.com/ we especially like the navigation look and feel.
The site needs to be clean and simple to find information and navigate and as such would like the site design elements to reflect this in its layout and element interplay.
This site will act as an information gateway for the member's, but also offer abilities to purchase memberships, get information on up coming events and purchase tickets to these events, and interact with the members on the site.
Hi All designers,
The client has now agreed to make the project funding guaranteed, so I hope to see some great designs from you.
Thanks
Sorry all, I hadn't uploaded the logo, has now been uploaded.
Hi all designers, please don't let the wireframe layout include restrict your design freedom on the page layout. We included this to give you a feel for the elements wanted in the site, but not to push you to have them all in that arrangement. Feel free to move around or remove parts of to make better use of the space.
Also this site is for ex-students who are members of an association linked to the school, and not for the school itself, so your designs need to lean towards a member, events and reunions type site design.
After a review today, client now requires that the sites Events need special consideration. Want to see in a prominent position on the landing page area a good area to showcase the upcoming events. Please take this into consideration in your future design layouts.
Hi All Designers, I appreciate all the new and current designs, and sorry a bit behind on the feedback, have been a bit swamped on my own workload, I will give feedback to you all, and will maybe look at an extension of the deadline if need be, as to also allow the clients to look over designs.
Thanks
Reason: Extending the project deadline to allow more feedback to be provider to all designers, to allow review by clients and the feedback through myself.
Reason: Client was un-available for comment, and want them to be able to give feedback to designers for last round updates.
Reason: Sorry all, client has been overseas, and will only be back next week, so need to extend the deadline to allow for client input next week.
Reason: Sorry client has be delayed overseas, so when be needing to work through the designs next week to allow full ability to give all designs due recognition.
Reason: Waiting for client to review designs.
Target Market(s)
Professionals from all varity of job types
Industry/Entity Type
Events
Requirements
Must have
- Please use the attached Logo in the design and look to use the current colour pallet as much as possible, but open to colour and pallet additions or amendments.
Must have a “hero” header image scroller for ability to showcase upcoming events and other items (Required for home/landing pages, could be amended or removed on inner pages).
Should look to follow the include wire frame layout concept as a good conception starting point - but do not limit to just this layout, use design discretion.
Include prominently positioned events area in layout for upcoming events to push the events heavy aspect of the site.
Should include icons/link abilities to access social sites and applications. Ie Chatterloop etc.
Nice to have
- A modern look with an edge to it.
Creative use of the sites colour pallet and site elements.
Should not have
- should not be a copy of the wireframe with colour added

```html
<!DOCTYPE html>
<html lang="en">
<head>
<meta charset="utf-8">
<title>Kestrelvale High School Old Boys Association</title>
<link rel="stylesheet" href="https://fonts.googleapis.com/css2?family=Open+Sans:wght@400;600;700&family=Oswald:wght@500;600&family=Ubuntu:wght@400;500&display=swap">
<style>
:root{
  --crimson:#8c0033;
  --crimson-dark:#5e0020;
  --crimson-text:#9b0b3c;
  --green:#0b6b45;
  --green-dark:#064a2f;
  --ink:#222;
  --body:#4a4a4a;
  --rule:#dcdcdc;
  --footer:#1f1e1f;
  --footer-deep:#121212;
  --muted:#9a9a9a;
}
*{box-sizing:border-box;margin:0;padding:0}
html,body{width:958px;height:1200px;overflow:hidden}
body{
  position:relative;
  font-family:"Open Sans",Arial,sans-serif;
  color:var(--body);
  background:linear-gradient(90deg,var(--crimson-dark) 0,var(--crimson) 12%,var(--crimson) 88%,var(--crimson-dark) 100%);
}
a{color:inherit;text-decoration:none}
.abs{position:absolute}

/* header */
.site-header{position:absolute;left:0;top:0;width:958px;height:71px;background:linear-gradient(#fff,#e9e9e9);border-bottom:1px solid #cfcfcf}
.brand{left:108px;top:14px;font-family:"Ubuntu",sans-serif;font-weight:500;font-size:40px;letter-spacing:-1px;color:#2a2a2a;line-height:48px}
.search-label{left:626px;top:12px;font-size:11px;color:#777;letter-spacing:.5px}
.search-box{left:674px;top:8px;width:175px;height:22px;border:1px solid #bdbdbd;background:#fff;font-size:10px;color:#999;padding:3px 6px}
.search-box svg{position:absolute;right:5px;top:4px}
.main-nav{right:108px;top:48px;display:flex;font-size:11.5px;color:#222}
.main-nav a{padding:0 10px;border-left:1px solid #ccc;line-height:13px}
.main-nav a:first-child{border-left:0}
.main-nav a:last-child{padding-right:0}
.main-nav .current{color:var(--crimson-text)}

/* page column */
.page{left:108px;top:71px;width:742px;height:1023px;background:#fff}

/* hero */
.hero{left:123px;top:101px;width:710px;height:257px;border:1px solid #ddd;padding:5px;background:#fff;box-shadow:0 6px 8px -6px rgba(0,0,0,.35)}
.hero-photo{width:100%;height:100%;background:linear-gradient(#cfe0ef 0,#e7eef3 25%,#7b4a3c 34%,#6b3f34 52%,#5f8a3e 66%,#7ea04b 100%)}
.hero-panel{left:530px;top:140px;width:270px;height:176px;background:rgba(140,0,51,.88);padding:14px 16px;color:#fff}
.hero-panel h1{font-family:"Oswald",sans-serif;font-weight:600;line-height:1;text-transform:uppercase}
.hero-panel .small{font-size:23px;display:block}
.hero-panel .big{font-size:38px;display:block;margin-top:4px}
.hero-panel p{font-size:10.5px;line-height:15px;margin-top:12px}
.hero-panel .btn-light{display:inline-block;margin-top:12px;background:#fff;color:var(--green-dark);font-size:10px;font-weight:700;padding:5px 7px}
.hero-arrow{top:215px;width:22px;height:30px;background:#3b3b3b;border:1px solid #fff}
.hero-arrow svg{display:block;margin:8px auto 0}

/* section headings */
.h-section{font-family:"Ubuntu",sans-serif;font-weight:400;font-size:16px;color:var(--ink)}
.para{font-size:10.5px;line-height:15px;color:var(--body)}
.rule{height:1px;background:var(--rule)}
.link-green{color:var(--green);font-weight:600}
.btn-green{display:inline-block;background:var(--green);color:#fff;font-size:10px;font-weight:700;padding:6px 9px;letter-spacing:.2px}

.img-block{border-radius:3px}
.news-photo{left:123px;top:387px;width:228px;height:150px;background:linear-gradient(#b98fb6,#8d6f8f 30%,#2d2a2a 55%,#1c1c1c)}
.news-copy{left:365px;top:383px;width:216px}
.news-copy .para{margin:8px 0 11px}

.about{left:123px;top:563px;width:458px}
.about .para{margin-top:8px}
.about .accent{color:var(--crimson-text)}

.ribbon{left:101px;top:726px;width:450px;height:40px}
.ribbon-title{left:124px;top:733px;font-family:"Ubuntu",sans-serif;font-size:18.5px;color:#fff;letter-spacing:.2px}

.member{left:123px;width:458px}
.member h3{font-family:"Ubuntu",sans-serif;font-weight:400;font-size:15.5px;color:var(--ink)}
.member .thumb{position:absolute;left:0;top:26px;width:113px;height:85px;border:5px solid #d4d1c8;background:linear-gradient(#9aa49b,#6f6d62 50%,#3d3a36)}
.member .thumb.hall{background:linear-gradient(#b98fb6,#7b6a7e 40%,#242424)}
.member .view{position:absolute;left:0;top:117px;width:113px;text-align:center;font-size:10px;font-weight:600;color:var(--green-dark)}
.member .para{position:absolute;left:125px;top:24px;width:333px}

/* sidebar */
.divider{left:595px;top:387px;width:1px;height:683px;background:#e3e3e3}
.side{left:611px;width:224px}
.cta{left:611px;top:388px;width:224px;height:55px;background:linear-gradient(#1b8a5c,#0a5a39);border-radius:3px;color:#fff;text-align:center;font-family:"Ubuntu",sans-serif;box-shadow:0 3px 4px rgba(0,0,0,.25)}
.cta .small{display:block;font-size:12px;margin-top:8px;font-weight:500}
.cta .big{display:block;font-size:19px;font-weight:500;line-height:22px}
.ticket{position:absolute;left:0;width:224px;height:66px;border-bottom:1px solid var(--rule)}
.ticket h4,.side-member h4{font-size:10.5px;font-weight:700;color:var(--crimson-text)}
.ticket .para{width:180px;margin-top:2px}
.ticket svg{position:absolute;right:0;top:4px}
.side-link{text-align:right;font-size:10px;font-weight:700;color:var(--green-dark);letter-spacing:.3px}
.side-member{position:absolute;left:0;width:224px}
.side-member .thumb{position:absolute;left:0;top:2px;width:60px;height:52px;background:linear-gradient(#9d8ca4,#3b3538 60%,#262224)}
.side-member .text{position:absolute;left:69px;top:0;width:155px}
.side-member .text h4{font-size:11.5px;font-weight:400;margin-bottom:3px}
.gallery-thumb{position:absolute;top:0;width:104px;height:63px;border:5px solid #d4d1c8}

/* footer */
.site-footer{left:108px;top:1094px;width:742px;height:106px;background:var(--footer)}
.footer-bottom{left:108px;top:1155px;width:742px;height:45px;background:var(--footer-deep);border-top:1px solid #000}
.footer-nav{left:123px;top:1100px;display:flex;font-size:9.5px;color:#9a9a9a;letter-spacing:.3px}
.footer-nav a{padding:0 15px;border-left:1px solid #666;line-height:11px}
.footer-nav a:first-child{padding-left:0;border-left:0}
.contact-label{left:123px;top:1121px;font-size:11.5px;font-weight:700;color:#fff}
.contact-number{left:123px;top:1138px;font-size:9.5px;color:#8a8a8a;letter-spacing:.4px}
.follow{left:742px;top:1097px;font-size:11.5px;color:#ddd;letter-spacing:.3px}
.social{left:742px;top:1117px;display:flex;gap:6px}
.social span{width:18px;height:18px;border-radius:2px}
.copyright{left:123px;top:1165px;font-size:10px;color:#ccc}
.copyright .accent{color:var(--crimson-text)}
.legal{right:123px;top:1165px;display:flex;gap:18px;font-size:10px;color:#ddd}
.legal a{text-decoration:underline}
</style>
</head>
<body>

<header class="site-header">
  <a class="abs brand" href="#">kvhsoba</a>
  <span class="abs search-label">SEARCH</span>
  <div class="abs search-box">Enter Your Keywords
    <svg width="13" height="13" viewBox="0 0 13 13"><circle cx="5.5" cy="5.5" r="4" fill="none" stroke="#888" stroke-width="1.5"/><line x1="8.5" y1="8.5" x2="12" y2="12" stroke="#888" stroke-width="1.8"/></svg>
  </div>
  <nav class="abs main-nav">
    <a class="current" href="#">HOME</a><a href="#">NEWS</a><a href="#">EVENTS</a><a href="#">PHOTOS</a><a href="#">MEMBERSHIP</a><a href="#">CONTACT</a>
  </nav>
</header>

<main class="abs page"></main>

<section class="abs hero">
  <div class="hero-photo" role="img" aria-label="Photo of the school's red brick main building above green lawns and a car park"></div>
</section>
<div class="abs hero-panel">
  <h1><span class="small">The Association</span><span class="big">of Excellence</span></h1>
  <p>Lorem ipsum dolor sit amet, consectetur adipiscing elit. Duis nec nisl id nunc laoreet.</p>
  <a class="btn-light" href="#">READ MORE</a>
</div>
<a class="abs hero-arrow" style="left:119px" href="#"><svg width="8" height="12"><path d="M7 1 2 6l5 5" fill="none" stroke="#fff" stroke-width="2"/></svg></a>
<a class="abs hero-arrow" style="left:814px" href="#"><svg width="8" height="12"><path d="M1 1l5 5-5 5" fill="none" stroke="#fff" stroke-width="2"/></svg></a>

<div class="abs img-block news-photo" role="img" aria-label="Photo of students seated in an assembly hall listening to a speaker"></div>
<section class="abs news-copy">
  <h2 class="h-section">Upcoming News &amp; Events</h2>
  <p class="para">Lorem ipsum dolor sit amet, consectetur adipi scing elit. Duis nec nisl id nunc laoreet rhoncus eget sed felis. Fusce accumsan nisl eu massa semper gravida.</p>
  <a class="btn-green" href="#">VIEW NEWS AND EVENTS</a>
</section>

<div class="abs rule" style="left:123px;top:552px;width:458px"></div>

<section class="abs about">
  <h2 class="h-section">About kvhs<span class="accent">oba</span></h2>
  <p class="para">Ut facilisis tempor turpis, eleifend tempor augue imperdiet vitae. Ut consectetur sapien ut erat lobortis blandit. Cras luctus, risus id scelerisque sagittis, nunc nunc tempus velit, sit amet rutrum nulla neque sed lectus. Aenean nec sem mauris. Sed tellus erat, lobortis in scelerisque at, tempor non augue. Sed risus mi, auctor id gravida ut, condimentum at lorem.</p>
  <p class="para">Donec sagittis lorem sed ligula consequat dignissim. Curabitur dolor neque, laoreet a malesuada ac, viverra vitae justo. Phasellus venenatis luctus nisi, ac gravida nisl rhoncus quis. Suspendisse condim entum odio ac mi consectetur interdum. Donec imperdiet lobortis aliquet...<a class="link-green" style="font-weight:400" href="#">read more</a></p>
</section>

<svg class="abs ribbon" viewBox="0 0 450 40" aria-hidden="true">
  <polygon points="0,0 12,6 12,40 0,34" fill="#053b25"/>
  <polygon points="12,0 430,0 450,20 430,40 12,40" fill="#0b6b45"/>
  <polygon points="12,0 430,0 440,10 12,10" fill="#1a7f55"/>
</svg>
<h2 class="abs ribbon-title">ASSOCIATION OF EX-STUDENT MEMBERS</h2>

<article class="abs member" style="top:778px;height:135px">
  <h3>Warren Ashby</h3>
  <div class="thumb" role="img" aria-label="Photo of members gathered in a glass-roofed hall"></div>
  <a class="view" href="#">View Member</a>
  <p class="para">Lorem ipsum dolor sit amet, consectetur adipiscing elit. Curabitur pulvinar eros in arcu fermentum nec pharetra tortor venen atis. Etiam nec elit augue. Etiam ac lacus nisl, at ultrices turpis. Pellentesque nec mauris vel urna accumsan adipiscing. Aenean justo quam, hendrerit at fringilla ut, venenatis nec erat. Sed vitae enim sed mauris imperdiet ultricies.</p>
</article>
<div class="abs rule" style="left:123px;top:919px;width:458px"></div>
<article class="abs member" style="top:931px;height:135px">
  <h3>Colin Marsh</h3>
  <div class="thumb hall" role="img" aria-label="Photo of students in an assembly hall"></div>
  <a class="view" href="#">View Member</a>
  <p class="para">Lorem ipsum dolor sit amet, consectetur adipiscing elit. Curabitur pulvinar eros in arcu fermentum nec pharetra tortor venen atis. Etiam nec elit augue. Etiam ac lacus nisl, at ultrices turpis. Pellentesque nec mauris vel urna accumsan adipiscing. Aenean justo quam, hendrerit at fringilla ut, venenatis nec erat. Sed vitae enim sed mauris imperdiet ultricies.</p>
</article>

<div class="abs divider"></div>

<a class="abs cta" href="#"><span class="small">CLICK HERE TO INTERACT</span><span class="big">WITH THE MEMBERS</span></a>
<div class="abs rule" style="left:611px;top:457px;width:224px"></div>

<section class="abs side" style="top:466px;height:240px">
  <h2 class="h-section">Event Tickets</h2>
  <div class="ticket" style="top:32px">
    <h4>Esent bibendum</h4>
    <p class="para">Duis faucibus felis nec eros ullam vcorper luctus...</p>
    <svg width="22" height="22" viewBox="0 0 22 22"><path d="M2 1l9 10-9 10M11 1l9 10-9 10" fill="none" stroke="#b8cddb" stroke-width="3.5"/></svg>
  </div>
  <div class="ticket" style="top:98px">
    <h4>Vestibulum ultricies mauris</h4>
    <p class="para">Nunc pharetra lectus et est luctus convallis. Suspendisse potenti...</p>
    <svg width="22" height="22" viewBox="0 0 22 22"><path d="M2 1l9 10-9 10M11 1l9 10-9 10" fill="none" stroke="#b8cddb" stroke-width="3.5"/></svg>
  </div>
  <div class="ticket" style="top:164px">
    <h4>Aenean blandit dolor</h4>
    <p class="para">Donec fermentum tempus risus, quis pretium ligula lacinia vitae....</p>
    <svg width="22" height="22" viewBox="0 0 22 22"><path d="M2 1l9 10-9 10M11 1l9 10-9 10" fill="none" stroke="#b8cddb" stroke-width="3.5"/></svg>
  </div>
  <a class="side-link abs" style="left:0;top:224px;width:224px" href="#">Purchase Events Tickets &gt; &gt;</a>
</section>
<div class="abs rule" style="left:611px;top:708px;width:224px"></div>

<section class="abs side" style="top:718px;height:200px">
  <h2 class="h-section">Our Members</h2>
  <div class="side-member" style="top:30px">
    <div class="thumb" role="img" aria-label="Photo of students seated in a hall"></div>
    <div class="text"><h4>Dean Holloway</h4><p class="para">Nunc pharetra lectus et est luctu convallis. Suspendisse potenti Nam dignissim eros... <a class="link-green" style="font-weight:400" href="#">read more</a></p></div>
  </div>
  <div class="rule abs" style="left:0;top:99px;width:224px"></div>
  <div class="side-member" style="top:112px">
    <div class="thumb" style="background:linear-gradient(#9aa49b,#6f6d62 50%,#3d3a36)" role="img" aria-label="Photo of members in a glass-roofed hall"></div>
    <div class="text"><h4>Neil Carrow</h4><p class="para">Ut nec aliquet dui. Curabitur volutpat massa at urna placerat vel luctus orci...<a class="link-green" style="font-weight:400" href="#">read more</a></p></div>
  </div>
  <div class="rule abs" style="left:0;top:181px;width:224px"></div>
  <a class="side-link abs" style="left:0;top:189px;width:224px" href="#">Purchase Membership &gt;&gt;</a>
</section>
<div class="abs rule" style="left:611px;top:925px;width:224px"></div>

<section class="abs side" style="top:934px;height:140px">
  <h2 class="h-section">Photo Gallery Of Members</h2>
  <div style="position:absolute;left:0;top:33px;width:224px;height:63px">
    <div class="gallery-thumb" style="left:2px;background:linear-gradient(#9aa49b,#6f6d62 50%,#3d3a36)" role="img" aria-label="Gallery photo of members in a glass-roofed hall"></div>
    <div class="gallery-thumb" style="left:120px;background:linear-gradient(#b98fb6,#7b6a7e 40%,#242424)" role="img" aria-label="Gallery photo of an assembly in the school hall"></div>
  </div>
  <div class="rule abs" style="left:0;top:112px;width:224px"></div>
  <a class="side-link abs" style="left:0;top:119px;width:224px" href="#">View Members Photo &gt;&gt;</a>
</section>
<div class="abs rule" style="left:611px;top:1070px;width:224px"></div>

<footer>
  <div class="abs site-footer"></div>
  <nav class="abs footer-nav"><a href="#">HOME</a><a href="#">NEWS</a><a href="#">EVENTS</a><a href="#">PHOTOS</a><a href="#">MEMBERSHIP</a><a href="#">CONTACT</a></nav>
  <div class="abs contact-label">Contact Number</div>
  <div class="abs contact-number">1-555-0142-7788</div>
  <div class="abs follow">Follow Us</div>
  <div class="abs social" aria-label="Social links">
    <span style="background:#3b5a98"></span>
    <span style="background:#3fa9e0"></span>
    <span style="background:#1b7ab5"></span>
    <span style="background:#c4302b"></span>
  </div>
  <div class="abs footer-bottom"></div>
  <p class="abs copyright">© Copyright 2012 <span class="accent">KVHSOBA</span>. All rights reserved</p>
  <nav class="abs legal"><a href="#">Privacy Statement</a><a href="#">Terms of Use</a><a href="#">Site Map</a></nav>
</footer>

</body>
</html>
```